Shadows over Briarwick Hall

We are hosting an open-to-the-public murder mystery dinner and masquerade ball on Oct. 31. I need a postcard design that we can display, hand out and mail for marketing.

We produce events in the KC area.

I'd like to see designs with a Halloween masquerade ball/murder mystery theme.

```html
<!DOCTYPE html>
<html lang="en">
<head>
<meta charset="utf-8">
<title>Shadows over Briarwick Hall — Postcard</title>
<link href="https://fonts.googleapis.com/css2?family=Creepster&family=Arimo:wght@700&display=swap" rel="stylesheet">
<style>
  :root {
    --page: #ffffff;
    --forest-deep: #0c1c1c;
    --forest-mid: #3d6a68;
    --forest-mist: #9cc3bd;
    --moon: #e6efe9;
    --ember: rgba(255, 150, 30, 0.75);
    --ember-soft: rgba(230, 110, 20, 0.35);
    --sign-dark: #333832;
    --sign-light: #68706a;
    --plank-gap: rgba(15, 18, 16, 0.75);
    --post: #4a4336;
    --gold: #fcc92a;
    --ink-white: #ffffff;
    --band: rgba(28, 30, 30, 0.78);
  }
  html, body {
    margin: 0;
    width: 1200px;
    height: 900px;
    overflow: hidden;
    background: var(--page);
  }
  .postcard {
    position: absolute;
    left: 83px;
    top: 50px;
    width: 1034px;
    height: 802px;
    overflow: hidden;
    background: var(--forest-deep);
  }
  .forest-scene {
    position: absolute;
    inset: 0;
    background:
      /* full moon glow */
      radial-gradient(circle 70px at 250px 80px, var(--moon) 0%, rgba(230,239,233,0.6) 60%, transparent 100%),
      radial-gradient(ellipse 330px 260px at 250px 100px, rgba(200,220,214,0.55), transparent 70%),
      /* lantern glows */
      radial-gradient(ellipse 46px 34px at 72px 112px, var(--ember), transparent 100%),
      radial-gradient(ellipse 60px 46px at 112px 612px, var(--ember), transparent 100%),
      radial-gradient(ellipse 44px 32px at 355px 585px, var(--ember), transparent 100%),
      radial-gradient(ellipse 56px 42px at 462px 672px, var(--ember), transparent 100%),
      radial-gradient(ellipse 70px 52px at 300px 690px, var(--ember-soft), transparent 100%),
      radial-gradient(ellipse 44px 34px at 812px 556px, var(--ember), transparent 100%),
      radial-gradient(ellipse 40px 32px at 862px 518px, var(--ember), transparent 100%),
      /* misty clearing */
      radial-gradient(ellipse 520px 360px at 500px 420px, rgba(156,195,189,0.55), transparent 75%),
      /* dark tree masses at the sides */
      linear-gradient(90deg, rgba(10,22,22,0.9) 0%, rgba(10,22,22,0.2) 14%, transparent 28%, transparent 74%, rgba(10,22,22,0.35) 86%, rgba(10,22,22,0.92) 100%),
      linear-gradient(180deg, rgba(10,22,22,0.55) 0%, transparent 18%),
      linear-gradient(180deg, var(--forest-mid) 0%, #4e7b77 40%, #3a5a44 70%, #1c3024 100%);
  }
  .sign-board {
    position: absolute;
    left: 222px;
    top: 162px;
    width: 560px;
    height: 398px;
    background:
      linear-gradient(180deg,
        transparent 0 108px, var(--plank-gap) 108px 112px,
        transparent 112px 204px, var(--plank-gap) 204px 208px,
        transparent 208px 300px, var(--plank-gap) 300px 304px,
        transparent 304px),
      linear-gradient(180deg, var(--sign-light) 0%, var(--sign-dark) 100%);
    box-shadow: 0 6px 18px rgba(0,0,0,0.5);
  }
  .sign-post {
    position: absolute;
    left: 472px;
    top: 560px;
    width: 50px;
    height: 132px;
    background: linear-gradient(90deg, #3a352c, var(--post));
  }
  .headline {
    position: absolute;
    left: 0;
    right: 0;
    top: 136px;
    margin: 0;
    text-align: center;
    font-family: "Creepster", cursive;
    font-weight: 400;
    color: var(--gold);
    text-shadow: 0 3px 6px rgba(0,0,0,0.75);
  }
  .headline-main {
    display: block;
    font-size: 118px;
    line-height: 1;
    letter-spacing: 4px;
  }
  .headline-sub {
    display: block;
    font-size: 60px;
    line-height: 1.1;
    margin-top: 4px;
  }
  .headline-small {
    font-size: 32px;
    margin-right: 8px;
  }
  .event-lines {
    position: absolute;
    left: 0;
    right: 0;
    top: 332px;
    margin: 0;
    text-align: center;
    font-family: "Creepster", cursive;
    font-size: 33px;
    line-height: 41px;
    letter-spacing: 1.5px;
    color: var(--ink-white);
    text-shadow: 0 2px 4px rgba(0,0,0,0.75);
  }
  .event-date {
    position: absolute;
    left: 0;
    right: 0;
    top: 468px;
    margin: 0;
    text-align: center;
    font-family: "Creepster", cursive;
    font-size: 62px;
    letter-spacing: 2px;
    color: var(--gold);
    text-shadow: 0 3px 6px rgba(0,0,0,0.75);
  }
  .contact-band {
    position: absolute;
    left: 0;
    right: 0;
    bottom: 0;
    height: 110px;
    padding-top: 4px;
    box-sizing: border-box;
    background: var(--band);
    color: var(--ink-white);
    font-family: "Arimo", Arial, sans-serif;
    font-weight: 700;
    font-size: 18px;
    line-height: 23.5px;
    text-align: center;
  }
  .contact-band p { margin: 0; }
</style>
</head>
<body>
  <main class="postcard">
    <div class="forest-scene" role="img" aria-label="Moonlit misty Halloween forest with bare twisted trees, bats, falling autumn leaves and glowing carved jack-o'-lanterns scattered on the ground"></div>
    <div class="sign-board" role="img" aria-label="Weathered wooden plank signboard draped with cobwebs"></div>
    <div class="sign-post" role="img" aria-label="Wooden sign post"></div>

    <h1 class="headline">
      <span class="headline-main">SHADOWS</span>
      <span class="headline-sub"><span class="headline-small">OVER</span>BRIARWICK HALL</span>
    </h1>

    <p class="event-lines">
      OPEN-TO-THE-PUBLIC<br>
      MURDER MYSTERY DINNER<br>
      AND MASQUERADE BALL
    </p>

    <p class="event-date">31 OCTOBRE 2014</p>

    <footer class="contact-band">
      <p>PHONE: 816-555-0147</p>
      <p>WEBSITE: WWW.NIGHTFALLKC.COM</p>
      <p>THE OVERLOOK AT FERNHILL 2100 N ALDER DR. KANSAS CITY, MO 64116</p>
    </footer>
  </main>
</body>
</html>
```